Wordpress Design Project - IT Consulting Services Web Site

Our are starting a new technology services company. We will provide services in software implementation and business intelligence.

We need a beautiful Wordpress web site design. We need a design for the homepage, and one interior content page.

The site must have a very professional and polished look and feel. What I have suggested below are things that I think work, but I am not a designer and I am open to your professional opinions. Please be willing to use your best judgment.

The homepage should have the following elements:
- A Header Area that includes:
o The company logo, and
o navigation (consistent with the interior page)
o a social media link section that includes rss feeds, youtube, facebook, linkedin and tweets
- A Body that includes:
o A slider
o An area that features up to six of the most recent or important posts including a thumbnail and small picture, a title, and a short excerpt for each.
o An area for around 100 words of text and an image
- A footer that includes:
o The company logo
o Contact information

The interior page is relatively simple. It should include the same navigation element as the homepage, and accommodate a one column text layout.

The current site …
You can visit the current site at www.korvelpath.com I built the current site using the “Velthor Quick Pane” premium theme. If you visit this site you get a sense of some of the things I am talking about, but there are things that I do not like about the current site. Here’s what I like and what I don’t like.

What I like about the current site:
- It is reactive – it adapts to the size of the viewing browser
- It has a “metro” feel to it. The company will have an association with Microsoft and having a “metro” theme is a plus, but not a requirement.
- It is different without being hard to navigate – the site the slider is from the “glide cascade widget”, the posts are represented with tiles and rearrange themselves when a topic is selected.

What I don’t like:
- The site lacks a cohesive feel – it feels to me like a bunch of different elements without a single theme that pulls everything together.
- It is not aesthetically appealing to me.
- The tiles in the post section are too big.
- I don’t like the white background – I would prefer a background color and ideally a background that somehow incorporates the graphic in the logo.

About themes
As I said, I used a Velthor theme in my design. I will be happy to continue using this theme, or would be willing to buy a new premium theme, so long as the cost is less than $100 U.S.

Site Map:
What we do
ERP Implementation
Business Intelligence
Who we are
What’s different about us
Principles
Mission, Vision, Values
Actions
How we work
What’s Different About Us
Blogs
What Papers
Presentations
Join
What we are looking for
What are you looking for?
Benefits
Context
Updates

Regarding Pictures
Please do not feel you need to use any of the pictures currently on the site.  Use whatever pictures you feel look best.  Comps are okay. 

It is not necessary to use any of the content on the current site - you do not need to use either the pictures or the text.  Please feel free to use pictures of your choice (comps okay), and/or lorem text.

The top level navigation is the navigation I would like.

Hello all,

Since this is a Wordpress project, it goes without saying I will need to implement this design in Wordpress.  It is not absolutely necessary that a design that matches an existing template (free or not), but a design that does will have an advantage over a design which requires that a new template be coded from scratch.

Thank you.

Target Market(s)

Business executives and potential employees

Industry/Entity Type

Software

Requirements
Nice to have
• It would be nice if the site was reactive.

```html
<!DOCTYPE html>
<html lang="en">
<head>
<meta charset="utf-8">
<title>KorvelPath — Software Implementation and Business Intelligence</title>
<link href="https://fonts.googleapis.com/css2?family=Roboto:wght@300;400;500&family=Arvo&display=swap" rel="stylesheet">
<style>
:root{
  --brand:#0a90d2;
  --brand-dark:#067fbd;
  --ink:#2a2a2a;
  --muted:#9a9a9a;
  --tile-ink:#163a57;
  --page:#f1f1f1;
  --rule:#c9c9c9;
  --white:#ffffff;
}
*{margin:0;padding:0;box-sizing:border-box}
html,body{width:928px;height:1200px;overflow:hidden}
body{position:relative;font-family:"Roboto",Arial,sans-serif;background:var(--page);color:var(--ink)}
.abs{position:absolute}

/* header + hero */
.hero{left:0;top:0;width:928px;height:430px;background:radial-gradient(ellipse at 50% 40%,#ffffff 0%,#f3f3f3 55%,#dedede 100%)}
.logo{display:flex;align-items:center;gap:6px;font-weight:300;font-size:20px;color:#8a8f94;letter-spacing:-.5px}
.logo b{font-weight:300;color:var(--brand)}
.logo .dot{width:12px;height:12px;border-radius:50%;background:var(--brand)}
.social{display:flex;gap:1px}
.social span{width:16px;height:16px;display:block}
.s1{background:#3b5a9a}.s2{background:#1da1f2}.s3{background:#d8322a}.s4{background:#0b74b3}
.mainnav{left:504px;top:35px;width:270px;height:27px;border-bottom:1px solid var(--brand);display:flex}
.mainnav a{flex:1;text-align:center;text-decoration:none;color:var(--muted);border-left:1px dotted #bdbdbd;line-height:1}
.mainnav a:first-child{border-left:none}
.mainnav strong{display:block;font-weight:300;font-size:12.5px}
.mainnav small{display:block;font-size:6px;margin-top:2px;color:#a8a8a8}
.hero-kicker{left:183px;top:124px;font-weight:300;font-size:14px;color:var(--brand)}
.hero-title{left:182px;top:136px;font-weight:400;font-size:29px;color:#9b9b9b;letter-spacing:-.5px}
.hero-tail{left:400px;width:146px;text-align:right;top:163px;font-weight:300;font-size:13px;color:var(--brand)}
.hero-visual{left:182px;top:90px;width:530px;height:302px;border-radius:6px;background:linear-gradient(180deg,rgba(255,255,255,0) 0%,rgba(225,225,228,.7) 60%,rgba(240,240,240,0) 100%)}
.slide-arrow{top:196px}
.filters{left:0;top:415px;width:928px;height:28px}
.filters .rule{position:absolute;left:0;top:15px;width:928px;height:1px;background:#8d8d8d}
.filters nav{position:absolute;left:266px;top:0;width:397px;height:27px;background:#fff;border:1px solid #555;display:flex;justify-content:center;align-items:center;font-size:8.5px}
.filters a{color:var(--brand);text-decoration:none;padding:0 6px;border-left:1px dotted #999}
.filters a:first-child{border-left:none}

/* tiles */
.tiles{left:0;top:448px;width:928px;height:270px;background:var(--brand)}
.tile{position:absolute;width:160px;text-align:center;font-family:"Arvo",Georgia,serif;font-size:11px;line-height:15px;color:var(--tile-ink)}
.tile svg{display:block;margin:0 auto 4px}
.vline{position:absolute;top:30px;width:1px;height:220px;background:var(--brand-dark)}
.hline{position:absolute;left:0;top:129px;width:928px;height:1px;background:var(--brand-dark)}
.strip{left:0;top:718px;width:928px;height:25px;background:linear-gradient(#dcdcdc,#ececec);border-bottom:1px solid var(--rule)}

/* content */
.content{left:0;top:743px;width:928px;height:261px;background:radial-gradient(ellipse at 50% 50%,#fafafa,#ececec);border-bottom:1px solid var(--rule)}
.eyebrow{font-size:9.5px;color:#222;letter-spacing:-.2px}
.section-title{font-weight:300;font-size:28px;color:var(--brand);letter-spacing:-.3px}
.copy{font-size:10.6px;line-height:15.5px;color:#333;width:620px}

/* footer */
.footer{left:0;top:1030px;width:928px;height:170px;background:var(--brand);color:var(--white)}
.footer h3{position:absolute;font-weight:300;font-size:14.5px}
.footer ul{position:absolute;list-style:none;font-size:7.3px;line-height:12.4px}
.footer li{color:#e3f2fb}
.contact li{display:flex;align-items:center;gap:4px}
.contact-with{left:632px;top:14px;display:flex;align-items:center;gap:6px;font-weight:300;font-size:10.5px}
.footer .logo{color:#ffffff}
.footer .logo b{color:#ffffff;font-weight:300}
.footer .logo .dot{background:#ffffff}
</style>
</head>
<body>

<header class="abs hero">
  <div class="abs logo" style="left:154px;top:34px"><span>Korvel<b>Path</b></span><span class="dot"></span></div>
  <div class="abs social" style="left:708px;top:6px" aria-label="Social links"><span class="s1"></span><span class="s2"></span><span class="s3"></span><span class="s4"></span></div>
  <nav class="abs mainnav">
    <a href="#"><strong>What</strong><small>what we do</small></a>
    <a href="#"><strong>Who</strong><small>who we are</small></a>
    <a href="#"><strong>How</strong><small>how we work</small></a>
    <a href="#"><strong>Join</strong><small>join us</small></a>
    <a href="#"><strong>Contact</strong><small>contact us</small></a>
  </nav>

  <div class="abs hero-visual" role="img" aria-label="Business team with laptops standing around a rising bar chart with an orange growth arrow"></div>
  <p class="abs hero-kicker">Software</p>
  <h1 class="abs hero-title">Implementation and Business</h1>
  <p class="abs hero-tail">Intelligence</p>

  <svg class="abs slide-arrow" style="left:133px" width="24" height="46" viewBox="0 0 24 46"><polyline points="22,1 2,23 22,45" fill="none" stroke="#555" stroke-width="1" stroke-dasharray="1.5 1.5"/></svg>
  <svg class="abs slide-arrow" style="left:774px" width="24" height="46" viewBox="0 0 24 46"><polyline points="2,1 22,23 2,45" fill="none" stroke="#555" stroke-width="1" stroke-dasharray="1.5 1.5"/></svg>
</header>

<div class="abs filters">
  <div class="rule"></div>
  <nav>
    <a href="#">All</a><a href="#">Identity</a><a href="#">People</a><a href="#">Principles</a><a href="#">Servies</a><a href="#">Thought</a><a href="#">Leadership</a><a href="#">Values</a>
  </nav>
</div>

<section class="abs tiles">
  <div class="vline" style="left:287px"></div>
  <div class="vline" style="left:450px"></div>
  <div class="vline" style="left:618px"></div>
  <div class="hline"></div>

  <div class="tile" style="left:126px;top:30px">
    <svg width="40" height="42" viewBox="0 0 40 42" fill="#fff"><rect x="2" y="34" width="6" height="8"/><rect x="11" y="28" width="6" height="14"/><rect x="20" y="22" width="6" height="20"/><rect x="29" y="16" width="6" height="26"/><path d="M4 24 L26 6 L22 3 L34 1 L32 13 L29 9 L7 27Z"/></svg>
    Growth is Essential
  </div>
  <div class="tile" style="left:289px;top:30px">
    <svg width="42" height="42" viewBox="0 0 42 42" fill="#fff"><path d="M20 4 H38 V38 H20 V33 H33 V9 H20Z"/><path d="M2 18 H16 V11 L27 21 L16 31 V24 H2Z"/></svg>
    ERP implementation
  </div>
  <div class="tile" style="left:451px;top:30px">
    <svg width="42" height="42" viewBox="0 0 42 42" fill="#fff"><path d="M20 14 C12 6 4 10 3 16 C9 12 14 12 19 16 C15 20 12 26 12 31 H16 C17 25 19 20 22 16 C27 14 33 16 37 20 C37 12 28 8 22 12 C22 6 17 2 11 4 C16 5 19 9 20 14Z"/><path d="M2 38 C8 30 34 30 40 38 C40 40 2 40 2 38Z"/></svg>
    Respect the journey
  </div>
  <div class="tile" style="left:629px;top:30px">
    <svg width="42" height="42" viewBox="0 0 42 42" fill="#fff"><circle cx="15" cy="15" r="9"/><circle cx="29" cy="29" r="8"/><g stroke="#fff" stroke-width="4"><line x1="15" y1="2" x2="15" y2="28"/><line x1="2" y1="15" x2="28" y2="15"/><line x1="29" y1="18" x2="29" y2="40"/><line x1="18" y1="29" x2="40" y2="29"/></g><circle cx="15" cy="15" r="4" fill="var(--brand)"/><circle cx="29" cy="29" r="3.5" fill="var(--brand)"/></svg>
    Experties is more useful than authrity
  </div>

  <div class="tile" style="left:128px;top:154px">
    <svg width="42" height="42" viewBox="0 0 42 42" fill="#fff"><rect x="4" y="2" width="18" height="38"/><rect x="22" y="14" width="16" height="26"/><g fill="var(--brand)"><rect x="8" y="7" width="10" height="3"/><rect x="8" y="14" width="10" height="3"/><rect x="8" y="21" width="10" height="3"/><rect x="8" y="28" width="10" height="3"/><rect x="26" y="19" width="4" height="4"/><rect x="32" y="19" width="4" height="4"/><rect x="26" y="27" width="4" height="4"/><rect x="32" y="27" width="4" height="4"/></g></svg>
    Not like building a house
  </div>
  <div class="tile" style="left:289px;top:154px">
    <svg width="42" height="42" viewBox="0 0 42 42" fill="#fff"><path d="M21 10 C14 10 11 16 13 21 C14 24 16 25 16 29 H26 C26 25 28 24 29 21 C31 16 28 10 21 10Z"/><rect x="16" y="31" width="10" height="3"/><rect x="17" y="35" width="8" height="3"/><g stroke="#fff" stroke-width="2.5"><line x1="21" y1="1" x2="21" y2="6"/><line x1="4" y1="18" x2="9" y2="18"/><line x1="33" y1="18" x2="38" y2="18"/><line x1="9" y1="6" x2="12" y2="9"/><line x1="33" y1="6" x2="30" y2="9"/><line x1="9" y1="29" x2="12" y2="27"/><line x1="33" y1="29" x2="30" y2="27"/></g></svg>
    What's the idea?
  </div>
  <div class="tile" style="left:451px;top:154px">
    <svg width="42" height="42" viewBox="0 0 42 42" fill="#fff"><path d="M22 2 C11 2 5 10 7 19 L4 26 L8 27 L8 33 C8 35 10 36 13 36 L15 36 L15 41 L32 41 L32 31 C38 27 39 20 37 13 C35 6 29 2 22 2Z"/><circle cx="19" cy="15" r="5" fill="var(--brand)"/><circle cx="28" cy="24" r="4" fill="var(--brand)"/><circle cx="19" cy="15" r="2" fill="#fff"/><circle cx="28" cy="24" r="1.6" fill="#fff"/></svg>
    Business Intelligence
  </div>
  <div class="tile" style="left:629px;top:154px">
    <svg width="44" height="42" viewBox="0 0 44 42" fill="#fff"><circle cx="11" cy="15" r="5"/><circle cx="33" cy="15" r="5"/><circle cx="22" cy="12" r="6"/><path d="M2 31 C2 23 20 23 20 31Z"/><path d="M24 31 C24 23 42 23 42 31Z"/><path d="M11 31 C11 20 33 20 33 31Z"/></svg>
    People are always more than labels
  </div>
</section>

<div class="abs strip"></div>

<main class="abs content">
  <p class="abs eyebrow" style="left:154px;top:21px">PEOPLE, PROCESSES AND TOOLS</p>
  <h2 class="abs section-title" style="left:154px;top:30px">Putting People First</h2>
  <p class="abs copy" style="left:154px;top:71px">Every services firm is made up of people, processes and tools. At Korvel Path, we put people first, tailoring everything we do to find, hire, train, and keep the very best people. Because once you have the best people everything else follows.</p>

  <p class="abs eyebrow" style="left:154px;top:148px">KORVEL PATH</p>
  <h2 class="abs section-title" style="left:154px;top:158px">What's the idea?</h2>
  <p class="abs copy" style="left:154px;top:196px">The idea is an old one but a great one.&nbsp; Harlan Brooke Ames was an American writer credited with creating the phrase "The American Dream".&nbsp; It's the idea that your success should depend on your ability and achievements, not on where you started out.&nbsp; It's an idea we try to live up to.</p>
</main>

<footer class="abs footer">
  <h3 style="left:154px;top:10px">Site Map</h3>
  <ul style="left:154px;top:34px">
    <li>What we do</li><li>ERP Implementation</li><li>Business Intelligence</li><li>Who we are</li><li>What's different about us</li><li>Principles</li><li>Mission, Vision, Values</li><li>Actions</li><li>How we work</li>
  </ul>
  <ul style="left:300px;top:34px">
    <li>What's Different About Us</li><li>Blogs</li><li>What Papers</li><li>Presentations</li><li>Join</li><li>What we are looking for</li><li>What are you looking for?</li><li>Benefits</li><li>Context</li>
  </ul>

  <h3 style="left:449px;top:10px">Contact Information</h3>
  <ul class="contact" style="left:449px;top:34px">
    <li><svg width="7" height="7" viewBox="0 0 10 10" fill="#fff"><path d="M2 0 L4 3 L3 4 C4 6 5 7 6 7 L7 6 L10 8 L8 10 C4 10 0 6 0 2Z"/></svg>0800-555-0142</li>
    <li><svg width="7" height="7" viewBox="0 0 10 10" fill="#fff"><rect x="1" y="0" width="8" height="10"/><rect x="3" y="2" width="4" height="2" fill="var(--brand)"/></svg>0800-555-0143</li>
    <li><svg width="7" height="7" viewBox="0 0 10 10" fill="#fff"><rect x="0" y="2" width="10" height="6"/><polyline points="0,2 5,6 10,2" fill="none" stroke="var(--brand)"/></svg>info@korvelpath.com</li>
  </ul>

  <div class="abs contact-with">Contact with Us:
    <div class="social"><span class="s1"></span><span class="s2"></span><span class="s3"></span><span class="s4"></span></div>
  </div>

  <div class="abs logo" style="left:632px;top:136px"><span>Korvel<b>Path</b></span><span class="dot"></span></div>
</footer>

</body>
</html>
```